Thistlewood Candles, Hand-poured scented soy candles

Create a logo and label design to use on my vintage country farmhouse style, all natural, hand poured soy candle jars and apothecaries. Candles will be labeled in 4 different sizes so design must be adaptable, clean, simple, telegraphic and invoke interest in the product. Think Black lettering on white or black on kraft brown. Thistlewood is the area code for New Hampshire where we make them. The labels will need a prominent area for the scent of the candle to be listed that the eyes are drawn to. Primitive country in design? Use of state attractions? Jars are a square mason style 8 ounce and 16 ounce. Tarts are a clamshell. Lids are a 70-400 series 2.5" label area. Candles are white in a clear glass jar, black lids. There will be label design sizes of 3"x 2.5" 2.5" round, 1.5"x2.5"

Target Market(s)

primitive country, farmhouse, vintage, general home decor

Contact Information for Business Card

Thistlewood Candles, all natural soy candles, hand-poured in New Hampshire, logo, phone, address. Possibly match the main label.

Logo Text

Thistlewood Candles, all natural soy candles, hand-poured in New Hampshire, area for scent description and size of container.

Font styles to use
Serif
Script

Colors

Designer to choose colors to be used in the design.

Requirements
Must have
• simple and clean, country farmhouse with a bit of vintage thrown in. possibly multiple fonts to distinguish info from scent name
Nice to have
• at this time I am open to suggestions
• Prefer scent names or brand name in an older script?
• older copperplate/Spencerian?
Should not have
• cluttered, busy, too modern, multiple colors

```html
<!DOCTYPE html>
<html lang="en">
<head>
<meta charset="utf-8">
<title>Thistlewood Candles – Jar Labels</title>
<link rel="stylesheet" href="https://fonts.googleapis.com/css2?family=IM+Fell+English&family=Poiret+One&family=Cormorant+Garamond:wght@500&display=swap">
<style>
  :root {
    --page-bg: #eee9e2;
    --ink: #1f1a14;
    --ink-soft: #3a2f24;
    --amber-light: #d9a169;
    --amber-mid: #c17c40;
    --amber-dark: #8f5426;
    --linen-light: #ddd5c4;
    --linen-mid: #c9bfac;
    --linen-dark: #a99d86;
    --art-sepia: #6e4a2c;
  }
  * { box-sizing: border-box; margin: 0; padding: 0; }
  html, body {
    width: 1200px;
    height: 1200px;
    overflow: hidden;
    background: var(--page-bg);
  }
  .canvas {
    position: relative;
    width: 1200px;
    height: 1200px;
    display: flex;
    align-items: center;
    justify-content: center;
    gap: 60px;
  }
  .label {
    position: relative;
    width: 440px;
    height: 400px;
    color: var(--ink);
    overflow: hidden;
  }
  .label--honeysuckle {
    background: radial-gradient(ellipse at 50% 45%, var(--amber-light) 0%, var(--amber-mid) 60%, var(--amber-dark) 100%);
    font-family: "IM Fell English", Georgia, serif;
    text-align: center;
  }
  .label--pine {
    background: radial-gradient(ellipse at 45% 45%, var(--linen-light) 0%, var(--linen-mid) 65%, var(--linen-dark) 100%);
    font-family: "Poiret One", "Century Gothic", sans-serif;
  }
  .scent {
    position: absolute;
    left: 0; right: 0;
    text-align: center;
  }
  .label--honeysuckle .scent {
    top: 14px;
    font-size: 26px;
    color: var(--ink-soft);
    opacity: 0.75;
  }
  .label--pine .scent {
    top: 22px;
    font-family: "Cormorant Garamond", Georgia, serif;
    font-weight: 500;
    font-size: 20px;
  }
  .brand {
    position: absolute;
    left: 0; right: 0;
    font-weight: 400;
    line-height: 1;
  }
  .label--honeysuckle .brand {
    top: 52px;
    font-size: 46px;
    text-align: center;
  }
  .label--pine .brand {
    top: 92px;
    left: 22px;
    font-size: 44px;
  }
  .tagline {
    position: absolute;
    left: 0; right: 0;
  }
  .label--honeysuckle .tagline {
    top: 104px;
    font-size: 27px;
    text-align: center;
  }
  .label--pine .tagline {
    top: 148px;
    left: 30px;
    font-size: 22px;
  }
  .artwork {
    position: absolute;
    display: block;
  }
  .label--honeysuckle .artwork {
    left: 155px; top: 150px;
    width: 130px; height: 150px;
  }
  .label--pine .artwork {
    left: 250px; top: 10px;
    width: 150px; height: 330px;
  }
  .origin {
    position: absolute;
    left: 0; right: 0;
    text-align: center;
  }
  .label--honeysuckle .origin {
    top: 322px;
    font-size: 19px;
  }
  .label--pine .origin {
    top: 354px;
    font-size: 20px;
    color: var(--ink-soft);
  }
  .size {
    position: absolute;
    left: 0; right: 0;
    top: 352px;
    font-size: 17px;
    text-align: center;
    color: var(--ink-soft);
    opacity: 0.7;
  }
</style>
</head>
<body>
  <main class="canvas">
    <section class="label label--honeysuckle">
      <p class="scent">Honeysuckle</p>
      <h1 class="brand">Thistlewood Candles</h1>
      <p class="tagline">all natural soy candles</p>
      <svg class="artwork" viewBox="0 0 130 150" role="img" aria-label="Vintage engraving of a Victorian farmhouse">
        <defs>
          <linearGradient id="house-tone" x1="0" y1="0" x2="0" y2="1">
            <stop offset="0" stop-color="#8a5e37"/>
            <stop offset="1" stop-color="#5e3d22"/>
          </linearGradient>
        </defs>
        <rect width="130" height="150" fill="url(#house-tone)" opacity="0.55"/>
      </svg>
      <p class="origin">Hand-Poured in New Hampshire</p>
      <p class="size">8 ounces</p>
    </section>

    <section class="label label--pine">
      <p class="scent">Pine Scented</p>
      <h1 class="brand">Thistlewood Candles</h1>
      <p class="tagline">all natural soy candles</p>
      <svg class="artwork" viewBox="0 0 150 330" role="img" aria-label="Line drawing of a candle in a curled holder">
        <rect width="150" height="330" fill="#b8ad97" opacity="0.45"/>
      </svg>
      <p class="origin">Hand-Poured in New Hampshire</p>
    </section>
  </main>
</body>
</html>
```